Postcard Design -- Harbor Bridgeworks

Harbor Bridgeworks believes that when low-income immigrants acquire the right tools (skills and abilities), they can overcome poverty and build a pathway to success as new Americans. We accomplish this through our wraparound strategy, which offers a full range of services designed to help people overcome barriers to the acquisition of the skills and abilities they need to thrive. This process involves recognizing the diverse skills immigrants already possess, resolving immediate needs or problems, identifying opportunities for growth, and monitoring progress toward goals. As a result, clients are able to acquire the skills and abilities they need to thrive as new Americans.

We need a postcard design that follows the Harbor Bridgeworks brand, but also has a heartwarming/holiday feel to it with a cool factor. This postcard will be mailed as an insert with our appeal letter. The purpose of this postcard is to encourage donors who receive it to reuse/mail it to someone else and encourage them to donate to Harbor Bridgeworks.

Target Market(s)

Donors

Industry/Entity Type

Non-Profit

Font styles to use
Sans Serif

Requirements
Must have
• Our Colors: #3276b5 #9bcb3c #fece3e #f04a50
• Double sided Postcard:
• Front side:
• - A design that is welcoming and has a heartwarming/holiday feel to it
• - Our logo
• - and a message (examples: 'Thinking About You'.. 'Giving back to the community'.. 'Celebrate with us'.. 'Sharing the holiday spirit'.. 'Share the cheer'.. 'Invest in our community'..) I'm open to new ideas.
• Back side:
• - Mission Statement
• - We help low-income, Spanish-speaking immigrants acquire the tools they need to thrive.
• - Logo
• - site link (harborbridgeworks.org)
• - donation link (donate.harborbridgeworks.org)
• - Call to action (Invest in Harbor Bridgeworks Today!.. Wishing you Happy Holidays, join me in supporting New-Americans today.. etc)
• - Leave area available for sender info and person receiving info (like a regular postcard)
• - 5087310925
• -FB and Pathnote icon
Nice to have
• Postcard Final Dimension: 3.5"x5" (with bleed, PLEASE)
• PROJECT SPECIFICS
• Audience = Donors
• Message = Asking other to invest on Harbor Bridgeworks
• Product = Postcard Design 3.5"x5"
• Font = Sans Serif

```html
<!DOCTYPE html>
<html lang="en">
<head>
<meta charset="utf-8">
<title>Harbor Bridgeworks Holiday Postcard</title>
<link rel="stylesheet" href="https://fonts.googleapis.com/css2?family=Comic+Neue:wght@700&family=Questrial&display=swap">
<style>
  :root {
    --brand-blue: #3276b5;
    --brand-green: #9bcb3c;
    --brand-yellow: #fece3e;
    --brand-red: #f04a50;
    --ink: #1d1d1d;
    --white: #ffffff;
    --page: #ece8e2;
    --social-one: #35bfd6;
    --social-two: #3b5998;
  }
  * { box-sizing: border-box; margin: 0; padding: 0; }
  html, body { width: 1200px; height: 800px; overflow: hidden; }
  body {
    background: var(--page);
    display: flex;
    align-items: center;
    justify-content: center;
    gap: 30px;
  }
  .postcard {
    position: relative;
    width: 560px;
    height: 392px;
    background: var(--white);
    box-shadow: 0 6px 18px rgba(0,0,0,.18);
    overflow: hidden;
  }

  /* Back side */
  .back { font-family: "Comic Neue", "Comic Sans MS", cursive; font-weight: 700; }
  .back .appeal {
    height: 64px;
    background: var(--brand-yellow);
    display: flex; align-items: center; justify-content: center;
    text-align: center;
    font-size: 15px; line-height: 1.3;
    color: var(--ink);
    padding: 0 40px;
  }
  .back .brand-bar {
    height: 58px;
    display: flex; align-items: center; justify-content: space-between;
    padding: 0 18px 0 14px;
  }
  .brand { display: flex; align-items: center; gap: 8px; color: var(--brand-blue); }
  .brand-mark { width: 22px; height: 22px; background: var(--brand-blue); flex: none; }
  .back .brand-name { font-size: 26px; }
  .social { display: flex; gap: 14px; }
  .social-link { display: flex; align-items: center; gap: 6px; font-size: 13px; }
  .social-link::before {
    content: ""; width: 22px; height: 22px; border-radius: 50%; display: block;
  }
  .social-link.pathnote { color: var(--social-one); }
  .social-link.pathnote::before { background: var(--social-one); }
  .social-link.circlehub { color: var(--social-two); }
  .social-link.circlehub::before { background: var(--social-two); }
  .back .community-photo {
    position: relative;
    height: 146px;
    background: linear-gradient(180deg, #f3e7df 0%, #e8cfc0 45%, #dcb9a6 70%, #f4ebe6 100%);
  }
  .back .mission {
    position: absolute; right: 18px; bottom: 10px;
    text-align: right;
    color: var(--brand-red);
    font-size: 16px; line-height: 1.35;
  }
  .back .contact {
    height: 124px;
    background: var(--brand-green);
    padding: 14px 24px 0 0;
    display: flex; flex-direction: column; align-items: flex-end;
  }
  .contact .phone { color: var(--white); font-size: 26px; }
  .contact .site { color: var(--white); font-size: 18px; margin-top: 2px; }
  .contact .donate { color: var(--ink); font-size: 17px; margin-top: 14px; }

  /* Front side */
  .front { font-family: "Questrial", Arial, sans-serif; }
  .photo-grid {
    position: absolute; inset: 0 0 84px 0;
    display: grid;
    grid-template-columns: 160px 1fr 170px;
    grid-template-rows: 1fr 1fr;
  }
  .photo { display: block; }
  .family-portrait { grid-row: 1 / 3; background: linear-gradient(170deg, #b9c98a 0%, #e0a98a 35%, #9fb3d6 65%, #d9b39a 100%); }
  .snow-day { grid-column: 2 / 4; background: linear-gradient(110deg, #8a8a6e 0%, #2f4f96 28%, #f7f7f7 50%, #f2e6e0 62%, #6fa3c8 80%, #7c6e5a 100%); }
  .park-family { background: linear-gradient(180deg, #9ec267 0%, #e3b392 40%, #b8c4d6 65%, #6f9a4b 100%); }
  .garden-kids { background: linear-gradient(180deg, #b6cf7a 0%, #e8bda3 40%, #e25c9c 75%, #f0a8c8 100%); }
  .front .footer {
    position: absolute; left: 0; right: 0; bottom: 0; height: 84px;
    display: flex; align-items: center; gap: 18px;
    padding: 0 16px;
  }
  .front .brand-name { font-size: 21px; white-space: nowrap; }
  .front .messages { flex: 1; font-size: 12px; line-height: 1.45; color: var(--ink); text-align: right; }
</style>
</head>
<body>

<section class="postcard back" aria-label="Postcard back side">
  <div class="appeal">Invest in Harbor Bridgeworks Today!.. Wishing you Happy Holidays, join me in supporting New-Americans today..</div>
  <div class="brand-bar">
    <div class="brand"><span class="brand-mark"></span><span class="brand-name">Harbor Bridgeworks</span></div>
    <div class="social" aria-label="Social links">
      <span class="social-link pathnote">Pathnote</span>
      <span class="social-link circlehub">Circlehub</span>
    </div>
  </div>
  <div class="community-photo" role="img" aria-label="Faded photo of a smiling community crowd">
    <p class="mission">We help low-income,<br>Spanish-speaking immigrants acquire the tools they need to thrive.</p>
  </div>
  <div class="contact">
    <span class="phone">5087310925</span>
    <span class="site">harborbridgeworks.org</span>
    <span class="donate">Donate us: donate.harborbridgeworks.org</span>
  </div>
</section>

<section class="postcard front" aria-label="Postcard front side">
  <div class="photo-grid">
    <span class="photo family-portrait" role="img" aria-label="Photo of a family of four sitting together outdoors"></span>
    <span class="photo snow-day" role="img" aria-label="Photo of a couple posing beside a snowman"></span>
    <span class="photo park-family" role="img" aria-label="Photo of a family standing in a park"></span>
    <span class="photo garden-kids" role="img" aria-label="Photo of a mother with two daughters holding a seedling"></span>
  </div>
  <div class="footer">
    <div class="brand"><span class="brand-mark"></span><span class="brand-name">Harbor Bridgeworks</span></div>
    <p class="messages">'Thinking About You'.. 'Giving back to the community'.. 'Celebrate with us'.. 'Sharing the holiday spirit'.. 'Share the cheer'.. 'Invest in our community'..</p>
  </div>
</section>

</body>
</html>
```